Steady Harbor Stewardship Graphics

We need help to design a logo, graphics, layout that will represent a particular type of leadership consulting business that we are about to launch. The design/graphics should be able to be used for developing a brochure, web page, advertisements, letterhead, business cards, etc. The leadership consulting business that we are launching is called “Steady Harbor Stewardship.” We would like to start with the design of a brochure. We have enclosed a draft to give you some ideas about the type of graphics we are looking for. The graphics should include fonts, colors, pictures/symbols, and layout initially for the brochure only. There are three draft pictures/symbols that we have gotten from the internet for the attached brochure that may be copyrighted. We would like you to develop something similar, but original for each of the graphic’s. They each represent a theme/topic that we will be using. For example, the graphic for the section titled “What is Steady Harbor Stewardship?” has a picture/graphic that has a diverse group of people to represent the idea of Collective Leadership. It leaves out some of the facial features for each person in order to make sure that there are no similarities to real persons. We need something similar to this. The graphic for “Why is Steady Harbor Stewardship important?”, uses a picture of “ice” and a “mouse.” “Mice and Ice” is a key metaphor that we will use in our business. We need something to represent this concept. The same is true for the third picture that represents ripples in water. After design of the brochure we may seek additional help for the web page and other items.

Target Market(s)

Government and business organizations

Colors

Designer to choose colors to be used in the design.

Requirements
Must have
• Brochure Design
Nice to have
• Logos

```html
<!DOCTYPE html>
<html lang="en">
<head>
<meta charset="utf-8">
<title>Steady Harbor Stewardship – Trifold Brochure</title>
<link href="https://fonts.googleapis.com/css2?family=Open+Sans:wght@400;600;700;800&display=swap" rel="stylesheet">
<style>
  :root {
    --stage: #b4bdbf;
    --green-top: #7cb749;
    --green-mid: #3f9656;
    --teal-bottom: #0f6d6a;
    --band: #e8e9e8;
    --band-edge: #d4d6d5;
    --heading-green: #3f9a3c;
    --heading-teal: #17706a;
    --ink-dark: #2b2f2e;
    --white: #ffffff;
    --bullet: #d9e8cf;
  }
  * { box-sizing: border-box; margin: 0; padding: 0; }
  html, body { width: 1108px; height: 1200px; overflow: hidden; }
  body {
    background: var(--stage);
    font-family: "Open Sans", Arial, sans-serif;
    color: var(--white);
    position: relative;
  }
  .brochure-side {
    position: absolute;
    left: 24px;
    width: 1060px;
    height: 560px;
    display: flex;
    box-shadow: 0 6px 18px rgba(0,0,0,.18);
  }
  .brochure-side.outside { top: 28px; }
  .brochure-side.inside { top: 612px; }
  .panel {
    width: 353.33px;
    height: 100%;
    background: linear-gradient(180deg, var(--green-top) 0%, var(--green-mid) 55%, var(--teal-bottom) 100%);
    position: relative;
    overflow: hidden;
    display: flex;
    flex-direction: column;
  }
  .panel + .panel { border-left: 1px solid rgba(0,0,0,.12); }
  .panel-header {
    background: var(--band);
    border-bottom: 3px solid var(--band-edge);
    border-radius: 0 0 50% 50% / 0 0 18px 18px;
    text-align: center;
    padding: 14px 22px 16px;
  }
  .panel-header h2 {
    color: var(--heading-green);
    font-weight: 800;
    font-size: 17px;
    line-height: 1.15;
  }
  .inside .panel-header { padding: 22px 26px 26px; min-height: 150px; }
  .inside .panel-header h2 { color: var(--heading-teal); font-size: 18px; }
  .panel-header .lead {
    color: var(--ink-dark);
    font-size: 11px;
    font-weight: 600;
    line-height: 1.3;
    margin-top: 14px;
  }
  .panel-body { padding: 12px 26px 16px; font-size: 10.5px; line-height: 1.38; flex: 1; }
  .panel-body p { margin-bottom: 9px; }
  .centered { text-align: center; }
  .section-label {
    font-weight: 800;
    text-transform: uppercase;
    font-size: 10px;
    letter-spacing: .3px;
    margin: 9px 0 3px;
    text-align: center;
  }
  .lettered { list-style: none; margin-left: 6px; }
  .lettered li span { display: inline-block; width: 14px; opacity: .7; }
  .dotted { list-style: none; }
  .dotted li { position: relative; padding-left: 16px; }
  .dotted li::before {
    content: ""; position: absolute; left: 0; top: 3px;
    width: 9px; height: 9px; border-radius: 50%; background: var(--bullet);
  }
  .placeholder {
    border-radius: 8px;
    margin: 10px auto;
  }
  .gears-art {
    width: 250px; height: 120px;
    background: radial-gradient(circle at 30% 60%, #3e8a4e 0 38px, transparent 40px),
                radial-gradient(circle at 65% 30%, #2f7f55 0 30px, transparent 32px),
                radial-gradient(circle at 62% 78%, #2f7f55 0 28px, transparent 30px);
  }
  .contacts { margin-top: 10px; display: flex; gap: 10px; align-items: flex-start; }
  .contacts .icon { flex: none; }
  .contacts h3 { font-size: 11px; font-weight: 700; text-align: center; margin-bottom: 2px; }
  .contacts p { font-size: 10.5px; font-weight: 600; margin: 0; }

  /* cover */
  .cover-frame {
    position: absolute; inset: 16px 20px;
    border: 1px solid rgba(255,255,255,.75);
    display: flex; flex-direction: column; align-items: center;
  }
  .cover-name {
    margin-top: 130px;
    font-size: 36px; font-weight: 800; line-height: 1.1;
    text-align: center; color: var(--white);
    display: flex; align-items: center; gap: 12px; flex-direction: column;
  }
  .cover-name .mark {
    width: 26px; height: 26px; border-radius: 50%; background: var(--white);
  }
  .tagline {
    margin-top: 44px; width: 240px;
    border-top: 1px solid rgba(255,255,255,.7);
    border-bottom: 1px solid rgba(255,255,255,.7);
    padding: 12px 0; font-size: 14px; line-height: 1.35; text-align: center;
  }
  .cover-credit { margin-top: auto; margin-bottom: 16px; font-size: 13px; }

  .people-art { width: 300px; height: 150px; background: linear-gradient(180deg, #d9a86b 0%, #5a6f8a 55%, #2f6e3e 100%); }
  .ice-art { width: 180px; height: 130px; background: linear-gradient(160deg, #d6f0fb 0%, #8fd0ea 60%, #5cb3d8 100%); }
  .ripple-art { width: 220px; height: 120px; background: radial-gradient(ellipse at center, #ffffff 0%, #cfe8f3 45%, #8cc5df 70%, transparent 72%); }
  .caps { font-weight: 800; text-transform: uppercase; }
</style>
</head>
<body>

<section class="brochure-side outside">
  <article class="panel objectives">
    <header class="panel-header"><h2>Steady Harbor Stewardship (SHS) Objectives</h2></header>
    <div class="panel-body">
      <p class="centered">SHS is about cultivating and capturing collective leadership resources in order to help chart a course through the dangers and opportunities of our time. Its objectives are as follows:</p>
      <h3 class="section-label">Improve Organizational Navigation</h3>
      <ul class="lettered">
        <li><span>A</span>Avoid potential land mines</li>
        <li><span>B</span>Exploit opportunities</li>
      </ul>
      <h3 class="section-label">Increase Accountability</h3>
      <ul class="lettered">
        <li><span>A</span>Constituency Accountability</li>
        <li><span>B</span>Outcome Accountability</li>
        <li><span>C</span>Process Accountability</li>
      </ul>
      <h3 class="section-label">Enhance Cooperation</h3>
      <ul class="lettered">
        <li><span>A</span>Create strong connections</li>
        <li><span>B</span>Balance competition with cooperation</li>
        <li><span>C</span>Incorporate strong, diverse individuals</li>
      </ul>
      <div class="placeholder gears-art" role="img" aria-label="Illustration of three turning gears labelled Skillful Navigation, Leadership Influence and Leadership Influencers"></div>
    </div>
  </article>

  <article class="panel programs">
    <header class="panel-header"><h2>SHS Programs</h2></header>
    <div class="panel-body">
      <p class="centered">SHS's comprehensive approach to improving leadership is transformational. However, it need not be implemented in its entirety to realize its benefits. It can be customized to meet the needs of small to large groups.</p>
      <h3 class="section-label">What does it include?</h3>
      <ul class="dotted">
        <li>Day long or Half day workshops</li>
        <li>Multi-Day workshops</li>
        <li>Instruction and coaching</li>
      </ul>
      <h3 class="section-label">What are the programs about?</h3>
      <ul class="dotted">
        <li>Developing a SH Philosophy</li>
        <li>Executing SH Processes</li>
        <li>Growing SH Judgement</li>
        <li>Leadership Roles for Everyone</li>
        <li>Team Leadership</li>
        <li>Building a SH Culture</li>
      </ul>
      <h3 class="section-label">Who could benefit?</h3>
      <ul class="dotted">
        <li>Organizations</li>
        <li>Professional Associations</li>
        <li>Individuals, Teams and Small Groups</li>
      </ul>
      <h3 class="section-label">How can it help?</h3>
      <ul class="dotted">
        <li>Identify leadership strengths and weaknesses</li>
        <li>Address leadership training needs</li>
        <li>Develop organizational leadership capacity</li>
      </ul>
      <div class="contacts">
        <svg class="icon" width="26" height="26" viewBox="0 0 26 26" aria-hidden="true">
          <circle cx="13" cy="13" r="12" fill="#fff"/>
          <rect x="6.5" y="8.5" width="13" height="9" fill="none" stroke="#0f6d6a" stroke-width="1.4"/>
          <path d="M6.5 8.5 L13 13.5 L19.5 8.5" fill="none" stroke="#0f6d6a" stroke-width="1.4"/>
        </svg>
        <div>
          <h3>CONTACTS</h3>
          <p>Dana Ortiz: dana.ortiz@harborsteward.net</p>
          <p>Lee Marlow: lee.marlow@harborsteward.net</p>
        </div>
      </div>
    </div>
  </article>

  <article class="panel cover">
    <div class="cover-frame">
      <h1 class="cover-name"><span class="mark"></span>Steady Harbor Stewardship</h1>
      <p class="tagline">Identify and Engage the Collective Leadership in Your Organization</p>
      <p class="cover-credit">Dana Ortiz &amp; Lee Marlow</p>
    </div>
  </article>
</section>

<section class="brochure-side inside">
  <article class="panel what-is">
    <header class="panel-header">
      <h2>What is Steady Harbor Stewardship?</h2>
      <p class="lead">Leadership that cultivates and harvests collective human resources to help organizations navigate today's uncertain world</p>
    </header>
    <div class="panel-body centered">
      <p>Identifying, growing, and channeling human resources is the primary role of Leadership.</p>
      <div class="placeholder people-art" role="img" aria-label="Illustration of a diverse group of people seated together, representing collective leadership"></div>
      <p>Skillful navigation, improved accountability, and enhanced levels of cooperation are magnified when collective knowledge, wisdom, and creativity are employed.</p>
      <p>Most leadership literature revolves around building individual capabilities. SHS is about tapping into the often-latent collective leadership resources in organizations.</p>
    </div>
  </article>

  <article class="panel why-important">
    <header class="panel-header">
      <h2>Why is Steady Harbor Stewardship important?</h2>
      <p class="lead">Cooperative, accountable organizations that are on track are better prepared to respond to the unprecedented dangers and opportunities of today's world.</p>
    </header>
    <div class="panel-body centered">
      <p>It was ice that sunk the Titanic, the largest passenger ship afloat, on its maiden voyage in 1912.</p>
      <p>It was a mouse (not the furry kind) that revolutionized the personal computer industry in the 1980's.</p>
      <div class="placeholder ice-art" role="img" aria-label="Illustration of a mouse frozen inside a block of ice, the mice and ice metaphor"></div>
      <p>What do these two events have in common? They both involve course corrections. One to avoid the "ice", and the other to not miss the "mice".</p>
      <p>In a more amplified setting, today's organizations face ice fields of danger along with oceans of possibility. Without skillful navigation, an organization is either left adrift and missing opportunities, or is propelling toward unintended destinations with possible dire consequences.</p>
    </div>
  </article>

  <article class="panel how-it-works">
    <header class="panel-header">
      <h2>How does Steady Harbor Stewardship work?</h2>
      <p class="lead">By cultivating and deploying positive Collective Leadership Influence through constructive Collective Leadership Influencers.</p>
    </header>
    <div class="panel-body centered">
      <p>Like ripples through water, Leadership Influence penetrates an organization. Beneficial Leadership Influence has these characteristics; it must be positive, is both individual and collective, and both indirect and direct.</p>
      <div class="placeholder ripple-art" role="img" aria-label="Illustration of a water droplet falling into a pool and spreading ripples"></div>
      <p>Collective Leadership Influence begins with a <span class="caps">Collective Leadership Philosophy</span>, grows through <span class="caps">Collective Leadership Processes</span>, and matures with <span class="caps">Collective Leadership Judgement</span>.</p>
      <p>Who bears responsibility for propelling Collective Leadership Influence? Influence cannot happen without competent Influencers. The three most important are: individuals, teams, and culture.</p>
    </div>
  </article>
</section>

</body>
</html>
```